A resource brochure for seniors and their families/Maplecrest Resource Group

As we age, the journey can come with unexpected challenges and obstacles. Maplecrest Resource Group is here to provide seniors and their families with a road map to navigate those challenges and insure the journey is as smooth as possible. We are a company that offers 'one stop shop' resources for seniors who need assistance with selling their home, need home care support or need to find suitable senior housing living choices and much more. We need this brochure to showcase a caring, clear and clear way for families or individuals, many who have just lost a spouse/parent, to find resources during a very difficult and confusing time in their life. The final design should communicate caring support, a call to action (call us!), and showcase a professional and knowledgeable team that will gently support and be a guide to families and individuals who are trying to make big life choices within the senior care arena.
Updates

Project Deadline Extended Reason: To give more time for designers as the initial window seemed a little too short. Thank you!!! Added Friday, March 20, 2015

Target Market(s)

A mature market- SENIORS (75+) and their families (adult children 50+) who typically are going through life changes such as losing a spouse or having to make a move from their home into a Retirement Community.

Industry/Entity Type

Group

Font styles to use
Serif
Script

Requirements
Must have
• Showcase a thoughtful and caring mentality- 'we will take care of you" in a professional and knowledgeable way. Please make it clear what the message is - we can assist with selling a home, bringing support and care into the home, find more appropriate housing as well as any resources or tools needed throughout the senior care spectrum of resources. Must have our name, logo, website and address and we need one panel to be laid out as a mailer- our address on top left. (Please see attached rough draft for address- thank you!) Also- please keep the testimonial, which is attached inclusive of additional verbiage.
Nice to have
• An attractive senior (female) on the cover of the brochure with a 'What's Next?" feel to engage people to open the collateral and relate to the story and purpose of what we do. Showcase what our services are- we are a company that guides families to and through much needed resources as it relates to aging and the ever-changing needs of an elderly person. We want to be the experts and trusted by our clients and the tough decisions that come along with aging. We offer our referral services at no cost to our clients.
Should not have
• Should not sound slick, 'sales-y' or too pushy- we are trying to build a relationship and not 'over sell'...we want to be a trusted resource guide and a helping hand.

```html
<!DOCTYPE html>
<html lang="en">
<head>
<meta charset="utf-8">
<title>Maplecrest Senior Resource Group – Brochure</title>
<link rel="stylesheet" href="https://fonts.googleapis.com/css2?family=PT+Sans:wght@400;700&family=PT+Sans+Narrow:wght@400;700&display=swap">
<style>
  :root{
    --olive:#8f9a4f;
    --olive-dark:#7d8841;
    --orange:#f7ad1d;
    --orange-text:#f5a81c;
    --navy:#454a6b;
    --sky:#c5e1f1;
    --sky-pale:#e2f0f8;
    --cream:#eeedd3;
    --cream-edge:#c9cc9b;
    --lime:#d6dc4a;
    --ink:#3d3f55;
    --white:#ffffff;
  }
  *{box-sizing:border-box;margin:0;padding:0}
  html,body{width:1200px;height:877px;overflow:hidden;background:var(--white)}
  .brochure{position:relative;width:1200px;height:877px;overflow:hidden;background:var(--white);font-family:"PT Sans",sans-serif}
  .backdrop{position:absolute;inset:0}
  .photo{position:absolute}
  .photo--family{left:402px;top:22px;width:400px;height:300px;
    background:linear-gradient(135deg,#6d8e3e 0%,#a9c07a 35%,#c9c7b4 55%,#7f9852 100%)}
  .photo--portrait{left:802px;top:62px;width:398px;height:260px;
    background:linear-gradient(110deg,#4f7a2c 0%,#8fb35a 40%,#b9b4a4 70%,#e9e4d8 100%)}
  .photo--hands-back{left:0;top:738px;width:400px;height:139px;
    background:linear-gradient(90deg,#c9a48a 0%,#8a7b5c 35%,#6f6448 100%)}
  .photo--hands-cover{left:802px;top:738px;width:398px;height:139px;
    background:linear-gradient(90deg,#c9a48a 0%,#8a7b5c 40%,#6f6448 100%)}
  .mailer{position:absolute;left:0;top:0;width:360px;height:738px}
  .mailer__line{position:absolute;transform-origin:left top;transform:rotate(-90deg);
    color:var(--orange-text);font-family:"PT Sans",sans-serif;font-size:15px;line-height:20px;white-space:nowrap}
  .mailer__address{left:22px;top:712px}
  .mailer__brand{left:158px;top:712px;font-size:17px;line-height:22px}
  .mailer__brand .mark{display:inline-block;width:12px;height:12px;border-radius:50%;background:var(--orange);margin-right:8px;vertical-align:middle}
  .mailer__contact{left:276px;top:712px}
  .brand{position:absolute;color:var(--navy);font-family:"PT Sans",sans-serif;font-weight:400;text-align:center}
  .brand__mark{display:block;width:30px;height:30px;border-radius:50%;background:var(--orange);margin:0 auto 12px}
  .brand--inside{left:452px;top:340px;width:320px;font-size:32px;line-height:40px}
  .brand--cover{left:810px;top:510px;width:350px;font-size:34px;line-height:42px}
  .contact{position:absolute;left:458px;top:525px;width:324px;height:295px;border-radius:16px;
    background:var(--cream);border:5px solid var(--cream-edge)}
  .contact__title{position:absolute;left:45px;top:28px;width:214px;height:35px;background:var(--navy);
    color:var(--lime);font-family:"PT Sans Narrow",sans-serif;font-weight:700;font-size:24px;line-height:35px;text-align:center}
  .contact__row{position:absolute;left:0;display:flex;font-family:"PT Sans Narrow",sans-serif;font-weight:700;font-size:18px;line-height:26px}
  .contact__label{width:94px;text-align:right;padding-right:8px;color:var(--navy)}
  .contact__value{color:var(--ink)}
  .contact__row--address{top:92px}
  .contact__row--phone{top:200px;left:4px}
  .contact__row--email{top:243px;left:8px}
  .headline{position:absolute;left:848px;top:355px;font-family:"PT Sans",sans-serif;font-weight:700;font-size:46px;
    color:var(--orange);text-shadow:2px 2px 2px rgba(120,80,0,.45);white-space:nowrap}
</style>
</head>
<body>
<main class="brochure">
  <div class="photo photo--family" role="img" aria-label="Photo: smiling senior woman in a garden with her adult family"></div>
  <div class="photo photo--portrait" role="img" aria-label="Photo: senior woman looking thoughtfully upward among green leaves"></div>
  <div class="photo photo--hands-back" role="img" aria-label="Photo: caring hands holding an elderly hand"></div>
  <div class="photo photo--hands-cover" role="img" aria-label="Photo: caring hands holding an elderly hand"></div>

  <svg class="backdrop" width="1200" height="877" viewBox="0 0 1200 877" aria-hidden="true">
    <!-- top band, back panel -->
    <path d="M0 0H420V22C300 30 180 40 90 70C50 84 20 96 0 108Z" fill="var(--olive)"/>
    <path d="M0 108C30 94 70 80 120 66C70 84 30 100 0 118Z" fill="var(--orange)"/>
    <!-- top band over inside and cover -->
    <path d="M400 0H1200V52C1100 70 1000 68 900 60C760 48 600 30 400 22Z" fill="var(--olive)"/>
    <path d="M600 0H1200V12C1100 30 1000 40 900 36C800 30 700 14 600 0Z" fill="var(--olive-dark)"/>
    <path d="M620 0C720 18 820 34 920 38C1020 42 1110 28 1200 8V18C1110 40 1020 52 920 50C820 46 720 26 620 0Z" fill="var(--navy)"/>
    <path d="M800 58C900 66 1000 70 1100 62C1140 58 1170 54 1200 50V62C1140 68 1060 76 980 76C900 74 850 68 800 62Z" fill="var(--orange)"/>
    <!-- sky sweeps -->
    <path d="M402 322C480 300 620 296 760 320C950 352 1100 460 1200 600V720C1110 560 960 420 780 360C640 320 500 320 402 340Z" fill="var(--sky)"/>
    <path d="M402 322C520 292 700 300 860 330C1000 360 1120 420 1200 480V540C1110 460 980 390 840 360C690 330 540 320 402 330Z" fill="var(--sky-pale)"/>
    <!-- vertical divider bands -->
    <path d="M360 0H402V877H360C380 700 390 500 370 300C364 200 360 100 360 0Z" fill="var(--orange)"/>
    <path d="M398 0C430 200 430 420 470 600C500 720 540 800 600 877H548C490 800 450 720 420 600C390 460 390 200 398 0Z" fill="var(--olive)"/>
    <path d="M402 20C440 220 420 420 450 600C470 720 500 800 560 877H500C450 800 420 720 404 600C390 420 400 220 402 20Z" fill="var(--navy)"/>
    <!-- back panel bottom -->
    <path d="M0 735C120 740 260 736 372 700L380 740H0Z" fill="var(--white)"/>
    <!-- cover bottom curves -->
    <path d="M802 738C950 740 1100 730 1200 700V716C1100 744 950 752 802 748Z" fill="var(--orange)"/>
    <path d="M1000 877C1080 850 1150 820 1200 790V877Z" fill="var(--olive)"/>
    <path d="M960 877C1060 846 1140 808 1200 776V790C1150 820 1080 850 1000 877Z" fill="var(--navy)"/>
    <path d="M802 860C880 866 940 870 1000 877H802Z" fill="var(--olive)"/>
  </svg>

  <section class="mailer" aria-label="Mailer panel">
    <p class="mailer__line mailer__address">4820 Cedar Hollow Road<br>Suite C110<br>Brookfield, WA 98412</p>
    <p class="mailer__line mailer__brand"><span class="mark"></span>Maplecrest Senior Resource Group</p>
    <p class="mailer__line mailer__contact">(800) 555-0142<br>hello@maplecrestSRG.com</p>
  </section>

  <p class="brand brand--inside"><span class="brand__mark"></span>Maplecrest<br>Senior Resource Group</p>

  <section class="contact">
    <h2 class="contact__title">Contact information</h2>
    <div class="contact__row contact__row--address"><span class="contact__label">Address :</span><span class="contact__value">4820 Cedar Hollow Road<br>Suite C110<br>Brookfield, WA 98412</span></div>
    <div class="contact__row contact__row--phone"><span class="contact__label">Phone :</span><span class="contact__value">(800) 555-0142</span></div>
    <div class="contact__row contact__row--email"><span class="contact__label">Email :</span><span class="contact__value">hello@maplecrestSRG.com</span></div>
  </section>

  <h1 class="headline">What’s Next ?</h1>
  <p class="brand brand--cover"><span class="brand__mark"></span>Maplecrest<br>Senior Resource Group</p>
</main>
</body>
</html>
```